Tidal Fern Business Cards

We need something new, fun and exciting for business cards. Our current ones are just plain and we need a design that pops. We want name, position held, phone, email on the front, and a 20% discount on the back. I have also uploaded our old business cards creative to see what we are not wanting, and how boring they were and we want something jazzed up from this, cool design and catches people attention.

```html
<!DOCTYPE html>
<html lang="en">
<head>
<meta charset="utf-8">
<title>Tidal Fern Business Cards</title>
<link href="https://fonts.googleapis.com/css2?family=Quicksand:wght@300;400;500;700&display=swap" rel="stylesheet">
<style>
  :root {
    --navy: #1f3d6e;
    --navy-soft: #2b4a7a;
    --coral: #f07070;
    --white: #ffffff;
    --faint: #ececec;
    --ink: #1c1c1c;
    --backdrop: #e6e3df;
  }
  * { margin: 0; padding: 0; box-sizing: border-box; }
  html, body { width: 1200px; height: 1008px; overflow: hidden; }
  body {
    background: var(--backdrop);
    font-family: "Quicksand", sans-serif;
    position: relative;
  }
  .card {
    position: absolute;
    left: 190px;
    width: 820px;
    height: 469px;
    overflow: hidden;
    box-shadow: 0 6px 18px rgba(0,0,0,0.18);
  }
  .card--front { top: 24px; background: var(--white); }
  .card--back { top: 515px; background: var(--navy); }

  /* front */
  .front-motif {
    position: absolute;
    left: 300px; top: 200px;
    width: 330px; height: 269px;
    background: radial-gradient(ellipse at 50% 60%, var(--faint) 0%, rgba(236,236,236,0.4) 55%, rgba(255,255,255,0) 75%);
  }
  .identity { position: absolute; left: 70px; top: 70px; }
  .identity__name { font-size: 40px; color: var(--navy); font-weight: 300; line-height: 1.1; }
  .identity__name strong { font-weight: 700; }
  .identity__role { font-size: 22px; color: var(--coral); font-weight: 300; margin-top: 2px; }
  .contact { position: absolute; left: 70px; top: 180px; list-style: none; }
  .contact__item {
    display: flex; align-items: center; gap: 12px;
    font-size: 19px; font-weight: 500; color: var(--ink);
    margin-bottom: 12px;
  }
  .contact__item svg { width: 18px; height: 18px; fill: var(--coral); flex: none; }
  .brand--front {
    position: absolute; right: 70px; top: 250px;
    display: flex; align-items: center; gap: 14px;
  }
  .brand__name { font-size: 54px; font-weight: 700; color: var(--navy); letter-spacing: 0.5px; }
  .brand__dot { width: 22px; height: 22px; background: var(--coral); border-radius: 50%; }

  /* back */
  .back-motif {
    position: absolute; left: 90px; top: 0;
    width: 730px; height: 469px;
    background: radial-gradient(ellipse at 55% 45%, var(--coral) 0%, var(--coral) 38%, rgba(240,112,112,0.55) 58%, rgba(31,61,110,0) 78%);
  }
  .offer { position: absolute; left: 420px; top: 120px; color: var(--white); }
  .offer__brand { font-size: 56px; font-weight: 700; line-height: 1; }
  .offer__get { font-size: 26px; font-weight: 300; margin-top: 18px; }
  .offer__value { font-size: 52px; font-weight: 700; color: var(--coral); line-height: 1; background: var(--navy); display: inline-block; padding: 2px 8px; margin-left: -8px; }
  .offer__label { font-size: 26px; font-weight: 300; margin-top: 4px; }
  .offer__panel { background: var(--navy); padding: 24px 30px; border-radius: 8px; margin-left: -30px; margin-top: -24px; }
</style>
</head>
<body>
  <section class="card card--front" aria-label="Business card front">
    <div class="front-motif" role="img" aria-label="Faint brand leaf and heart decoration"></div>
    <div class="identity">
      <h1 class="identity__name"><strong>Your</strong> Name</h1>
      <p class="identity__role">Job Title</p>
    </div>
    <ul class="contact">
      <li class="contact__item">
        <svg viewBox="0 0 24 24"><path d="M6.6 10.8a15.1 15.1 0 0 0 6.6 6.6l2.2-2.2a1 1 0 0 1 1-.25 11.4 11.4 0 0 0 3.6.57 1 1 0 0 1 1 1V20a1 1 0 0 1-1 1A17 17 0 0 1 3 4a1 1 0 0 1 1-1h3.5a1 1 0 0 1 1 1c0 1.25.2 2.45.57 3.57a1 1 0 0 1-.25 1z"/></svg>
        000 000 0000
      </li>
      <li class="contact__item">
        <svg viewBox="0 0 24 24"><path d="M2 5h20v14H2z M2 5l10 8 10-8" stroke="#fff" stroke-width="1.5"/></svg>
        youremail@xyz.com
      </li>
      <li class="contact__item">
        <svg viewBox="0 0 24 24"><circle cx="12" cy="12" r="10"/><path d="M2 12h20M12 2c3 3 3 17 0 20M12 2c-3 3-3 17 0 20" stroke="#fff" stroke-width="1.3" fill="none"/></svg>
        www.yourwebsite.com
      </li>
    </ul>
    <div class="brand brand--front">
      <span class="brand__name">Tidal Fern</span>
      <span class="brand__dot"></span>
    </div>
  </section>

  <section class="card card--back" aria-label="Business card back">
    <div class="back-motif" role="img" aria-label="Large coral brand leaf and heart decoration"></div>
    <div class="offer">
      <div class="offer__panel">
        <p class="offer__brand">Tidal Fern</p>
        <p class="offer__get">Get</p>
        <p class="offer__value">20%</p>
        <p class="offer__label">Discount</p>
      </div>
    </div>
  </section>
</body>
</html>
```